MORVELINA movie poster

MORVELINA is an QSB (www.qsbacademy.net) thesis film, www.morvelinafilm.net, about a prisoner in Soviet prison camp who is looking for his wife.
Included are several stills, our film blurb, etc. Poster must be VERTICLE.

Poster should include the title "MORVELINA." It may also include the tag, "I only ask for one thing."

The movie is Black and White, btw the way, so the posters should not be very colorful.

NOTE: You do not need to use all the photos, of course. Whatever you think is most compelling, even if its only 1.

Movie

```html
<!DOCTYPE html>
<html lang="en">
<head>
<meta charset="utf-8">
<title>MORVELINA — Poster</title>
<link rel="stylesheet" href="https://fonts.googleapis.com/css2?family=Russo+One&family=Oswald:wght@400;500&display=swap">
<style>
  :root {
    --paper-light: #bdbdbd;
    --paper-mid: #a6a6a6;
    --paper-dark: #8a8a8a;
    --paper-shadow: #7d7d7d;
    --title-ink: rgba(236, 236, 236, 0.66);
    --tagline-ink: #f4f4f4;
    --credit-ink: #1c1c1c;
  }
  html, body {
    margin: 0;
    padding: 0;
    width: 786px;
    height: 1200px;
    overflow: hidden;
    background: var(--paper-mid);
  }
  .poster {
    position: relative;
    width: 786px;
    height: 1200px;
    overflow: hidden;
    background: var(--paper-mid);
  }
  .poster__still {
    position: absolute;
    inset: 0;
    background:
      radial-gradient(ellipse 34% 26% at 58% 46%, rgba(125,125,125,0.55) 0%, rgba(125,125,125,0) 100%),
      radial-gradient(ellipse 62% 50% at 64% 42%, var(--paper-dark) 0%, rgba(138,138,138,0.5) 55%, rgba(166,166,166,0) 82%),
      radial-gradient(ellipse 40% 30% at 12% 60%, rgba(125,125,125,0.45) 0%, rgba(125,125,125,0) 100%),
      radial-gradient(ellipse 50% 40% at 90% 8%, rgba(200,200,200,0.5) 0%, rgba(200,200,200,0) 100%),
      linear-gradient(165deg, var(--paper-light) 0%, var(--paper-mid) 45%, #9c9c9c 100%);
  }
  .poster__title {
    position: absolute;
    left: 0;
    top: 0;
    width: 786px;
    height: 1040px;
  }
  .poster__title text {
    font-family: "Russo One", sans-serif;
    font-size: 360px;
    fill: var(--title-ink);
  }
  .poster__tagline {
    position: absolute;
    left: 0;
    right: 0;
    top: 1064px;
    margin: 0;
    text-align: center;
    font-family: "Russo One", sans-serif;
    font-size: 22px;
    line-height: 26px;
    letter-spacing: 3px;
    color: var(--tagline-ink);
  }
  .credits {
    position: absolute;
    left: 146px;
    width: 494px;
    top: 1130px;
    font-family: "Oswald", sans-serif;
    font-weight: 400;
    color: var(--credit-ink);
    text-transform: uppercase;
  }
  .credits__line {
    display: flex;
    justify-content: space-between;
    align-items: center;
    height: 20px;
    font-size: 12.5px;
    line-height: 14px;
    white-space: nowrap;
  }
  .credits__item {
    flex-shrink: 0;
    display: inline-flex;
    align-items: center;
  }
  .credits__role {
    display: inline-flex;
    flex-direction: column;
    align-items: center;
    font-size: 4.5px;
    line-height: 5px;
    margin-right: 3px;
    flex-shrink: 0;
  }
  .credits__role--inline {
    font-size: 6.5px;
    line-height: 7px;
    margin: 0 4px;
  }
</style>
</head>
<body>
<main class="poster">
  <div class="poster__still" role="img" aria-label="Faded black-and-white still of the prisoner on textured grey paper with ink splatter"></div>

  <svg class="poster__title" viewBox="0 0 786 1040" aria-label="MORVELINA">
    <text x="39" y="440" textLength="726" lengthAdjust="spacingAndGlyphs">MOR</text>
    <text x="39" y="720" textLength="726" lengthAdjust="spacingAndGlyphs">VEL</text>
    <text x="39" y="1004" textLength="726" lengthAdjust="spacingAndGlyphs">INA</text>
  </svg>

  <p class="poster__tagline">I ONLY ASK FOR ONE THING.</p>

  <section class="credits">
    <div class="credits__line">
      <span class="credits__item">QSB Academy<span class="credits__role credits__role--inline">presents</span>"Morvelina"</span>
      <span class="credits__item">Dmitri Solvenko</span>
      <span class="credits__item">Pavel Ostrogin</span>
    </div>
    <div class="credits__line">
      <span class="credits__item">Lida Marova</span>
      <span class="credits__item">Yuri Belcov</span>
      <span class="credits__item">Oleg Tarkanov<span class="credits__role credits__role--inline">and</span>Ilya Varesh</span>
      <span class="credits__item"><span class="credits__role"><span>production</span><span>designer</span></span>Delphine Roscastell</span>
    </div>
    <div class="credits__line">
      <span class="credits__item"><span class="credits__role"><span>edited</span><span>by</span></span>Nora Feldvik</span>
      <span class="credits__item"><span class="credits__role"><span>cinematography</span><span>by</span></span>Warren J. Holcomb</span>
      <span class="credits__item"><span class="credits__role"><span>produced</span><span>by</span></span>Talia Benzimra</span>
      <span class="credits__item"><span class="credits__role"><span>written &amp; directed</span><span>by</span></span>Jonah Reitmann</span>
    </div>
  </section>
</main>
</body>
</html>
```